Cover for Where the Quiet River Bends Beyond Our Morning

Cover for a book that describes everything that happens to a person, from pre-birth life plans through growing in compassion and wisdom to death and living in the afterlife. The information is revealed in messages from people living in the life after this life. The title is Lanterns Along the Hidden Stair of Every Soul: Gathered from Voices Dwelling in the Further Meadow. Author is T. Morven Ashdale. Book size is 6 by 9.

Target Market(s)

General

Font styles to use
Serif

```html
<!DOCTYPE html>
<html lang="en">
<head>
<meta charset="utf-8">
<title>Lanterns Along the Hidden Stair of Every Soul — Full Cover</title>
<link rel="stylesheet" href="https://fonts.googleapis.com/css2?family=Oswald:wght@500;700&family=Lato:wght@400&display=swap">
<style>
  :root {
    --page: #ffffff;
    --sky-deep: #6b3d12;
    --sky-mid: #b97a2a;
    --sky-light: #f2cf7e;
    --sky-glow: #fff1c4;
    --portrait-grey: #8a8780;
    --portrait-dark: #3a3a36;
    --foliage: #2f4a2a;
    --boardwalk: #4a3a2c;
    --gold-light: #fff0a0;
    --gold-mid: #e0a82a;
    --gold-dark: #7a4a08;
    --ink-white: #ffffff;
    --shadow: rgba(30, 15, 0, 0.85);
  }
  html, body {
    margin: 0;
    padding: 0;
    width: 813px;
    height: 1200px;
    overflow: hidden;
    background: var(--page);
  }
  .cover-spread {
    position: absolute;
    left: 0;
    top: 305px;
    width: 813px;
    height: 589px;
    overflow: hidden;
    font-family: "Oswald", "Arial Narrow", sans-serif;
  }
  .cloud-sky {
    position: absolute;
    inset: 0;
    background:
      radial-gradient(ellipse 22% 22% at 12% 12%, var(--sky-glow), transparent 70%),
      radial-gradient(ellipse 20% 25% at 40% 35%, var(--sky-light), transparent 70%),
      radial-gradient(ellipse 25% 25% at 20% 80%, var(--sky-glow), transparent 70%),
      radial-gradient(ellipse 20% 20% at 95% 45%, var(--sky-light), transparent 70%),
      radial-gradient(ellipse 25% 25% at 85% 95%, var(--sky-glow), transparent 70%),
      linear-gradient(160deg, var(--sky-mid) 0%, var(--sky-deep) 45%, var(--sky-mid) 75%, var(--sky-light) 100%);
  }
  .portrait-art {
    position: absolute;
    left: 468px;
    top: 18px;
    width: 310px;
    height: 540px;
    border-radius: 46% 46% 30% 30% / 35% 35% 20% 20%;
    background:
      radial-gradient(ellipse 45% 30% at 55% 35%, var(--portrait-grey), transparent 75%),
      radial-gradient(ellipse 60% 30% at 50% 75%, var(--foliage), transparent 80%),
      linear-gradient(180deg, transparent 0%, var(--portrait-dark) 40%, var(--boardwalk) 85%, transparent 100%);
    opacity: 0.85;
    filter: blur(4px);
  }
  .gold-text {
    font-weight: 700;
    text-transform: uppercase;
    background: linear-gradient(180deg, var(--gold-light) 0%, var(--gold-mid) 45%, var(--gold-dark) 55%, var(--gold-mid) 80%, var(--gold-light) 100%);
    -webkit-background-clip: text;
    background-clip: text;
    color: transparent;
    filter: drop-shadow(2px 2px 2px var(--shadow));
  }
  .white-text {
    font-weight: 500;
    text-transform: uppercase;
    color: var(--ink-white);
    text-shadow: 1px 1px 2px var(--shadow);
  }
  .justified {
    text-align: justify;
    text-align-last: justify;
  }

  /* Back cover */
  .back-cover {
    position: absolute;
    left: 0;
    top: 0;
    width: 385px;
    height: 589px;
  }
  .back-author {
    position: absolute;
    left: 0;
    right: 0;
    top: 26px;
    margin: 0;
    text-align: center;
    font-size: 20px;
  }
  .back-title {
    position: absolute;
    left: 36px;
    top: 84px;
    width: 311px;
    margin: 0;
    font-size: 24px;
    line-height: 1.3;
  }
  .back-title span { display: block; }
  .back-subtitle {
    position: absolute;
    left: 36px;
    top: 182px;
    width: 311px;
    margin: 0;
    font-size: 12.5px;
  }
  .blurb {
    position: absolute;
    left: 45px;
    width: 295px;
    margin: 0;
    font-family: "Lato", "Helvetica", sans-serif;
    font-variant: small-caps;
    font-size: 14px;
    line-height: 15.5px;
    text-align: justify;
    text-align-last: center;
    color: var(--ink-white);
    text-shadow: 1px 1px 2px var(--shadow);
  }
  .blurb::first-letter { font-size: 22px; }
  .blurb--summary { top: 236px; }
  .blurb--more { top: 392px; }

  /* Spine */
  .spine {
    position: absolute;
    left: 385px;
    top: 0;
    width: 39px;
    height: 589px;
  }
  .spine-text {
    position: absolute;
    left: 9px;
    top: 26px;
    margin: 0;
    writing-mode: vertical-rl;
    white-space: nowrap;
    font-size: 14px;
    letter-spacing: 0.5px;
  }
  .spine-author { font-size: 16px; font-weight: 700; margin-bottom: 14px; }

  /* Front cover */
  .front-cover {
    position: absolute;
    left: 424px;
    top: 0;
    width: 389px;
    height: 589px;
  }
  .front-title {
    position: absolute;
    left: 40px;
    top: 310px;
    width: 311px;
    margin: 0;
  }
  .front-title span { display: block; line-height: 1.05; }
  .front-title .line-first { font-size: 31px; }
  .front-title .line-second { font-size: 37px; }
  .front-title .line-third { font-size: 59px; line-height: 1; }
  .front-subtitle {
    position: absolute;
    left: 40px;
    top: 468px;
    width: 311px;
    margin: 0;
    font-size: 12.5px;
  }
  .front-author {
    position: absolute;
    left: 40px;
    width: 311px;
    top: 540px;
    margin: 0;
    text-align: center;
    font-size: 18px;
  }
</style>
</head>
<body>
  <main class="cover-spread">
    <div class="cloud-sky" role="img" aria-label="Golden sunlit clouds spreading across back, spine and front"></div>

    <section class="back-cover">
      <p class="back-author white-text">T. Morven Ashdale</p>
      <h2 class="back-title gold-text">
        <span class="justified">Lanterns Along the Hidden</span>
        <span class="justified">Stair of Every Soul</span>
      </h2>
      <p class="back-subtitle white-text justified">Gathered from Voices Dwelling in the Further Meadow</p>
      <p class="blurb blurb--summary">This book describes everything that happens to a person, from pre-birth life plans through growing in compassion and wisdom to death and living in the afterlife. The information is revealed in messages from people living in the life after this life.</p>
      <p class="blurb blurb--more">Lorem ipsum dolor sit amet, consectetur adipiscing elit, sed do eiusmod tempor incididunt ut labore et dolore magna aliqua.</p>
    </section>

    <section class="spine">
      <p class="spine-text white-text"><span class="spine-author">T. Morven Ashdale</span>Lanterns Along the Hidden Stair of Every Soul</p>
    </section>

    <div class="portrait-art" role="img" aria-label="Black and white portrait of an older bearded man gazing upward, with hilltop crosses at sunset rising from his hair and a green-edged boardwalk path blended into his chest"></div>

    <section class="front-cover">
      <h1 class="front-title gold-text">
        <span class="line-first justified">Lanterns Along the</span>
        <span class="line-second justified">Hidden Stair of</span>
        <span class="line-third justified">Every Soul</span>
      </h1>
      <p class="front-subtitle white-text justified">Gathered from Voices Dwelling in the Further Meadow</p>
      <p class="front-author white-text">T. Morven Ashdale</p>
    </section>
  </main>
</body>
</html>
```